we need a design for Water Bottle Lable Wrap
The product is called Corvane Water is a restructured water. its a very healthy and rejuvenating water
we were looking at using as a tag ling Restore, Recover, Rejuvenate.

```html
<!DOCTYPE html>
<html lang="en">
<head>
<meta charset="utf-8">
<title>Corvane Water – Bottle Label Wrap</title>
<link rel="stylesheet" href="https://fonts.googleapis.com/css2?family=Poppins:wght@400;700&display=swap">
<style>
  :root {
    --backdrop: #d5d5d5;
    --label-navy: #1e2a66;
    --wave-light: #4a5aa3;
    --wave-deep: #26337a;
    --text-white: #ffffff;
  }
  html, body {
    margin: 0;
    padding: 0;
    width: 1005px;
    height: 1200px;
    overflow: hidden;
    background: var(--backdrop);
  }
  .canvas {
    position: relative;
    width: 1005px;
    height: 1200px;
  }
  .label-wrap {
    position: absolute;
    left: 50px;
    top: 373px;
    width: 905px;
    height: 453px;
    background: var(--label-navy);
    box-shadow: 0 3px 6px rgba(0, 0, 0, 0.25);
    overflow: hidden;
    font-family: "Poppins", sans-serif;
    color: var(--text-white);
  }
  .brand-name {
    position: absolute;
    left: 0;
    right: 0;
    top: 92px;
    margin: 0;
    text-align: center;
    font-weight: 700;
    font-size: 64px;
    line-height: 1.02;
    letter-spacing: 1px;
    color: var(--text-white);
  }
  .brand-name .brand-line {
    display: block;
  }
  .brand-name .brand-line--first {
    text-transform: none;
  }
  .brand-name .brand-line--second {
    text-transform: uppercase;
  }
  .tagline {
    position: absolute;
    left: 0;
    right: 0;
    top: 268px;
    margin: 0;
    text-align: center;
    font-weight: 400;
    font-size: 19px;
    letter-spacing: 0.3px;
  }
  .wave-band {
    position: absolute;
    left: 0;
    right: 0;
    bottom: 0;
    height: 142px;
    background: linear-gradient(180deg, var(--wave-light) 0%, #3a4a95 45%, var(--wave-deep) 100%);
  }
</style>
</head>
<body>
  <main class="canvas">
    <section class="label-wrap">
      <h1 class="brand-name">
        <span class="brand-line brand-line--first">Corvane</span>
        <span class="brand-line brand-line--second">Water</span>
      </h1>
      <p class="tagline">Restore, Recover, Rejuvenate</p>
      <div class="wave-band" role="img" aria-label="Decorative band of stylised ocean waves in pale blue line work"></div>
    </section>
  </main>
</body>
</html>
```